Home inventory company needs a single full page flyer design for a flyer that will be put into a pre

My company performs home inventory services in case of disaster, or for preparation to move, getting divorced or estate planning. During a free estimate, I will be giving a presentation folder to the customer with this flyer inside. This flyer will be informational in regards to why it is imperative to use my service now vs. later. It should also list the packages I offer, but prices should not go on the flyer as they are subject to change. Flyer should include my logo and colors of the logo. Flyer needs to stand out so unique design ideas are welcome. I see the flyer having a black / dark background and I see the text being a really bright green like in my logo. This is not set in stone though, I anticipate viewing other color schemes.

Target Market(s)

Anyone who lives in a home and owns things

Industry/Entity Type

It Company

Font styles to use
Sans Serif

Requirements
Must have
• My logo, my colors, my packages (without pricing) and some text indicating why my services are needed now vs. later.
Nice to have
• Creativeness with the logo in regards to where it is on the page. I would love to see a gauge or meter next to each home package showing how much coverage each package represents. The meter for the budget package would show that there is adequate coverage. The meter for the last package, grand tucked, would show a meter that is off the charts. In between the meters would show increasing coverage as we get to the end.
Should not have
• There should be nothing in the color white

```html
<!DOCTYPE html>
<html lang="en">
<head>
<meta charset="utf-8">
<title>Keeply Home Record Services Flyer</title>
<link href="https://fonts.googleapis.com/css2?family=Open+Sans:wght@400;600;700;800&display=swap" rel="stylesheet">
<style>
  :root {
    --bg: #2b2c2b;
    --bg-deep: #1c1d1c;
    --green: #7cc242;
    --green-dark: #4f8a25;
    --text: #c9cdc5;
    --muted: #9ea39a;
  }
  * { margin: 0; padding: 0; box-sizing: border-box; }
  html, body { width: 857px; height: 1200px; overflow: hidden; background: var(--bg-deep); }
  .flyer {
    position: relative; width: 857px; height: 1200px; overflow: hidden;
    background: var(--bg);
    font-family: "Open Sans", Arial, sans-serif; color: var(--text);
  }
  .hero-photo {
    position: absolute; left: 290px; top: 0; width: 567px; height: 520px;
    background: linear-gradient(180deg, #6f93b8 0%, #9db6c9 30%, #a98a6d 55%, #7b5a43 80%, #5a4a3a 100%);
  }
  .left-panel { position: absolute; left: 0; top: 0; width: 290px; height: 520px; overflow: hidden; }
  .brand { position: absolute; left: 30px; top: 92px; display: flex; align-items: center; gap: 10px; }
  .brand-square { width: 38px; height: 38px; background: var(--green); }
  .brand-name { font-size: 42px; font-weight: 800; color: var(--green); letter-spacing: 1px; line-height: 1; }
  .brand-tagline { position: absolute; left: 30px; top: 142px; font-size: 10px; color: var(--muted); }
  .contact { position: absolute; left: 30px; top: 190px; width: 250px; list-style: none; }
  .contact li { display: flex; align-items: center; gap: 10px; font-size: 17px; font-weight: 700; color: var(--green); height: 30px; margin-bottom: 12px; white-space: nowrap; }
  .contact svg { width: 20px; height: 20px; flex: none; }
  .intro { position: absolute; left: 30px; top: 335px; width: 245px; font-size: 14.5px; line-height: 1.45; font-weight: 600; color: var(--green); }
  .green-band { position: absolute; left: 0; top: 520px; width: 857px; height: 24px; background: var(--green); }
  .band-dark { position: absolute; left: 0; top: 544px; width: 270px; height: 186px; background: var(--bg-deep); }
  .room-photo { position: absolute; top: 544px; height: 186px; }
  .room-1 { left: 270px; width: 198px; background: linear-gradient(160deg, #d6c3a2, #8c6c4c); }
  .room-2 { left: 474px; width: 186px; background: linear-gradient(160deg, #c9b08a, #6e5038); }
  .room-3 { left: 666px; width: 191px; background: linear-gradient(160deg, #b89a78, #5e4030); }
  .room-strip { position: absolute; left: 0; top: 730px; width: 857px; height: 8px; background: var(--green-dark); }
  .details { position: absolute; left: 26px; top: 760px; width: 805px; display: grid; grid-template-columns: 262px 262px 255px; gap: 13px; }
  .package h2 { font-size: 11px; font-weight: 800; color: var(--green); text-transform: uppercase; margin: 0 0 4px; }
  .package h2 span { text-transform: none; font-weight: 600; }
  .package ul { list-style: none; margin-bottom: 12px; }
  .package li { font-size: 9.5px; line-height: 1.35; padding-left: 10px; position: relative; margin-bottom: 3px; }
  .package li::before { content: ""; position: absolute; left: 0; top: 5px; width: 4px; height: 4px; background: var(--green); }
  .why { font-size: 10px; line-height: 1.45; margin-bottom: 14px; }
  .footer-band { position: absolute; left: 0; bottom: 0; width: 857px; height: 18px; background: var(--green); }
</style>
</head>
<body>
<main class="flyer">
  <div class="hero-photo" role="img" aria-label="Photo of a multi-storey brick apartment building with balconies under a blue sky"></div>

  <div class="left-panel">
    <div class="brand"><span class="brand-square"></span><span class="brand-name">KEEPLY</span></div>
    <p class="brand-tagline">Keeply Home Record Services</p>

    <ul class="contact">
      <li><svg viewBox="0 0 24 24"><path fill="#7cc242" d="M6.6 10.8a15 15 0 0 0 6.6 6.6l2.2-2.2c.3-.3.7-.4 1-.2 1.1.4 2.3.6 3.6.6.6 0 1 .4 1 1V20c0 .6-.4 1-1 1A17 17 0 0 1 3 4c0-.6.4-1 1-1h3.5c.6 0 1 .4 1 1 0 1.3.2 2.5.6 3.6.1.3 0 .7-.2 1z"/></svg>555-014-2286</li>
      <li><svg viewBox="0 0 24 24"><rect x="2" y="5" width="20" height="14" fill="#7cc242"/><path d="M2 5l10 8 10-8" fill="none" stroke="#2b2c2b" stroke-width="2"/></svg>dana@keeplyhome.com</li>
      <li><svg viewBox="0 0 24 24"><circle cx="12" cy="12" r="10" fill="none" stroke="#7cc242" stroke-width="2"/><path d="M2 12h20M12 2c3 3 3 17 0 20M12 2c-3 3-3 17 0 20" fill="none" stroke="#7cc242" stroke-width="2"/></svg>www.keeplyhome.com</li>
    </ul>

    <p class="intro">Get in touch with Keeply Home Record Services (KEEPLY) in Phoenix, AZ for questions or to schedule a free consultation to see what package best meets your needs.</p>
  </div>

  <div class="green-band"></div>
  <div class="band-dark"></div>
  <div class="room-photo room-1" role="img" aria-label="Photo of a bright furnished living room"></div>
  <div class="room-photo room-2" role="img" aria-label="Photo of a living room with sofa and large windows"></div>
  <div class="room-photo room-3" role="img" aria-label="Photo of a furnished bedroom"></div>
  <div class="room-strip"></div>

  <section class="details">
    <div class="package">
      <h2>Apartment Package <span>(for apartments only)</span></h2>
      <ul>
        <li>Detailed photos and documentation of major rooms, such as kitchens and bedrooms</li>
        <li>Back-up copy of inventory on disc</li>
        <li>Full color printed inventory with report &amp; photos</li>
        <li>Up to 75 photos</li>
      </ul>
      <h2>Budget Package</h2>
      <ul>
        <li>Detailed photos and documentation of major rooms and key items in each area including appliances, furniture and electronics</li>
        <li>Back-up copy of inventory on disc</li>
        <li>Full color printed inventory with report</li>
        <li>Up to 150 photos</li>
      </ul>
      <h2>Half Tucked Package</h2>
      <ul>
        <li>Detailed photos and documentation of all household items, with serial numbers where available</li>
        <li>Back-up copy of inventory on disc</li>
        <li>Full color printed inventory with report</li>
      </ul>
    </div>
    <div class="package">
      <h2>Grand Tucked Package</h2>
      <ul>
        <li>Detailed photos and documentation of every item in the home, including closets, drawers, garage and attic</li>
        <li>Item descriptions, model and serial numbers</li>
        <li>Back-up copy of inventory on disc</li>
        <li>Full color printed inventory with report &amp; photos</li>
        <li>Up to 500 photos</li>
        <li>Secure online copy of inventory</li>
        <li>Annual update reminder and review</li>
        <li>Bonus: one free update within the first year</li>
        <li>Extra photos and rooms may be added for a small fee based on home size and number of items</li>
      </ul>
    </div>
    <div class="package">
      <p class="why">If your home has not been inventoried, now is the time. Disasters strike without warning, and after a loss it is nearly impossible to remember everything you owned. A current inventory speeds insurance claims, helps with moving, divorce and estate planning, and gives you peace of mind today.</p>
      <h2>Additional Services</h2>
      <ul>
        <li>Storage inventory: full photos of boxes and stored items</li>
        <li>Collectibles &amp; antiques: detailed photos and descriptions for appraisal</li>
        <li>Jewelry &amp; valuables: close up photos with notes</li>
        <li>Vehicle and boat inventory for insurance records</li>
        <li>Business inventory for offices and small shops</li>
        <li>Inventory update service as new items are added</li>
      </ul>
    </div>
  </section>

  <div class="footer-band"></div>
</main>
</body>
</html>
```